*** Bakery Needs a Business Card

I need a business card for my new bakery - Pine Lane Baking Dept. We make biscuits, cakes, muffins and other sweets. Our food is honest, wholesome and down to earth - i'd love this to be reflected in the design of the card. The design MUST include our logo (see the attached image - which needs to be replicated). The design should only use 2 or at most 3 colours.

Industry/Entity Type

Bakery

Requirements
Must have
• Must include my logo.
Must have a clean, simple design.
Space for my name, my title, my phone number, my facebook page (I will provide details later)
Should not have
• Must not have lots of bright colours.
Must not have any unnescassry graphics.

```html
<!DOCTYPE html>
<html lang="en">
<head>
<meta charset="utf-8">
<title>Pine Lane Baking Dept. – Business Card</title>
<link rel="stylesheet" href="https://fonts.googleapis.com/css2?family=Marcellus&family=Lato:wght@400;700&display=swap">
<style>
  :root {
    --page: #ffffff;
    --card-front: #cdc1c4;
    --card-front-light: #d9ced0;
    --card-back: #dccfd2;
    --card-back-light: #e6dbdd;
    --ink: #7a2745;
    --ink-soft: #8a3a55;
    --ink-faint: rgba(122, 39, 69, 0.32);
  }
  * { margin: 0; padding: 0; box-sizing: border-box; }
  html, body { width: 962px; height: 1200px; overflow: hidden; background: var(--page); }
  .canvas { position: relative; width: 962px; height: 1200px; }
  .card { position: absolute; left: 137px; width: 692px; height: 445px; overflow: hidden; }
  .card--front { top: 128px; background: var(--card-front); }
  .card--back { top: 616px; background: var(--card-back); }
  .card__pattern { position: absolute; inset: 0; }
  .card__pattern--front {
    background: radial-gradient(circle at 50% 45%, var(--card-front-light), var(--card-front) 75%);
  }
  .card__pattern--back {
    background: radial-gradient(circle at 50% 50%, var(--card-back-light), var(--card-back) 75%);
  }

  .company {
    position: absolute; top: 40px; left: 0; right: 0; text-align: center;
    font-family: "Marcellus", serif; font-weight: 400; font-size: 27px; letter-spacing: 3px; color: var(--ink);
  }
  .person { position: absolute; top: 148px; left: 50px; width: 240px; text-align: center; color: var(--ink); }
  .person__name { font-family: "Marcellus", serif; font-size: 25px; letter-spacing: 2px; line-height: 30px; }
  .person__title { font-family: "Lato", sans-serif; font-weight: 700; font-size: 16px; margin-top: 2px; color: var(--ink-soft); }
  .contact {
    position: absolute; top: 148px; right: 40px; width: 250px; text-align: center; color: var(--ink);
    font-family: "Lato", sans-serif; font-weight: 700; font-size: 20px; letter-spacing: 1px; line-height: 28px;
  }
  .contact__email { font-size: 19px; letter-spacing: 0.6px; }
  .brand {
    position: absolute; top: 272px; left: 0; right: 0; text-align: center;
    font-family: "Marcellus", serif; font-size: 44px; letter-spacing: 2px; color: var(--ink);
  }

  .repeat { position: absolute; inset: 0; }
  .repeat__name {
    position: absolute; white-space: nowrap;
    font-family: "Marcellus", serif; font-size: 30px; letter-spacing: 1px; color: var(--ink-faint);
  }
</style>
</head>
<body>
<main class="canvas">
  <section class="card card--front">
    <div class="card__pattern card__pattern--front" role="img" aria-label="Soft repeating floral damask pattern in pale mauve"></div>
    <h1 class="company">Pine Lane Baking Dept.</h1>
    <div class="person">
      <p class="person__name">Name Surname</p>
      <p class="person__title">Title</p>
    </div>
    <div class="contact">
      <p>T: 07700900456</p>
      <p class="contact__email">name@pinelane.com</p>
    </div>
    <p class="brand">Pine Lane</p>
  </section>

  <section class="card card--back">
    <div class="card__pattern card__pattern--back" role="img" aria-label="Soft repeating floral damask pattern in pale mauve"></div>
    <div class="repeat" aria-hidden="true">
      <span class="repeat__name" style="top:-4px; left:4px;">Pine Lane</span>
      <span class="repeat__name" style="top:-4px; left:268px;">Pine Lane</span>
      <span class="repeat__name" style="top:-4px; left:520px;">Pine Lane</span>

      <span class="repeat__name" style="top:46px; left:78px;">Pine Lane</span>
      <span class="repeat__name" style="top:46px; left:410px;">Pine Lane</span>

      <span class="repeat__name" style="top:96px; left:-30px;">Pine Lane</span>
      <span class="repeat__name" style="top:96px; left:240px;">Pine Lane</span>
      <span class="repeat__name" style="top:96px; left:560px;">Pine Lane</span>

      <span class="repeat__name" style="top:148px; left:120px;">Pine Lane</span>
      <span class="repeat__name" style="top:148px; left:440px;">Pine Lane</span>

      <span class="repeat__name" style="top:200px; left:-10px;">Pine Lane</span>
      <span class="repeat__name" style="top:200px; left:280px;">Pine Lane</span>
      <span class="repeat__name" style="top:200px; left:580px;">Pine Lane</span>

      <span class="repeat__name" style="top:254px; left:60px;">Pine Lane</span>
      <span class="repeat__name" style="top:254px; left:390px;">Pine Lane</span>

      <span class="repeat__name" style="top:308px; left:-20px;">Pine Lane</span>
      <span class="repeat__name" style="top:308px; left:230px;">Pine Lane</span>
      <span class="repeat__name" style="top:308px; left:540px;">Pine Lane</span>

      <span class="repeat__name" style="top:360px; left:110px;">Pine Lane</span>
      <span class="repeat__name" style="top:360px; left:420px;">Pine Lane</span>

      <span class="repeat__name" style="top:408px; left:0px;">Pine Lane</span>
      <span class="repeat__name" style="top:408px; left:260px;">Pine Lane</span>
      <span class="repeat__name" style="top:408px; left:560px;">Pine Lane</span>
    </div>
  </section>
</main>
</body>
</html>
```